Iphone and Android APP Screen Design - Word of the Day

We developed an iPhone app called “TradeLingo”. It displays one word each day to improve the users english skills for business use. in addition an archive containing older words is included. The app is fully functional and all features are already implemented. We need a design that expresses high quality with its elements clearly arranged.

Tasks:
1. Colours to be used in the design should be adapted to the webpage www.kelvora-press.de
• #872735 – link and background, #396588 - background, #376688 – links, #999999 – main navigation buttons, #f6f6f6 – background
• You DO NOT have to use all of these colours or use them in the same way as on the website

2. Designs of 4 Screens (Screenshots of the working app will be provided)
• Screen containing the word of the day, optionaly the translation, the type of the word (e.g. Verb), the explanation, an example phrase, the play button to listen to the pronunciation, an optional ad banner and the Kelvora Press logo
• Screen containing the archive of the last 365 words in a chronological order (selecting one word brings up a new screen looking like the word of today)
• Screen containing the archive of the last 365 day in an alphabetical order (selecting one word brings up a new screen looking like the word of today)
• Screen containing information about our company including a button opening a mobile landing page on the web and the Kelvora Press logo

3. Design of the loading Splash-Screen (also vectorbased, scaleable for different screen sizes)
• Simple, singlecolored Screen, with worldmap in the back and in front “TradeLingo”
• The Kelvora Press logo should be included
• Png file sizes: 320x480, 640x960, 320x480, 240x320, 480x800, 480x854, 240x400, 240x432

What 3 things do you want your company name to communicate to your customers?
Quality, reliability, success

List the names of your top three competitors:
http://www.plimbastore.com/android_applications/entertainment/word-of-the-day_qdvj.html
http://gadmerlist.com/education/french-word-of-the-day
http://gadmerlist.com/education/polish-word-of-the-day

Please tell us why nobody is submitting any designs. Too little payment or don't you understand the requirements? 

We posted another project just for the needed icons. Have a look there:
http://jobs.tavrinlo.com/job.aspx?id=4172

ok, here's the text that should be on the about page:

this is version one in english:
Kelvora Press
is a bi-monthly business English magazine for German-speakers who need to use English internationally in their jobs. As well as language topics, the magazine focuses on intercultural communication, careers, management and technology. The magazine is accompanied by a vocabulary supplement, an audio-CD, a workbook and the Website www.kelvora-press.de.

version two in german:
Kelvora Press
ist eine alle zwei Monate erscheinende Zeitschrift für Business-Englisch, die sich an deutsche Muttersprachler wendet, die Englisch im Beruf für ihre internationalen Geschäftsbeziehungen benötigen. Nicht nur sprachliche Themen, sondern auch interkulturelle Kommunikation, Karriere und berufliche Laufbahn, Management und neue Technologien stehen im Mittelpunkt. Zu jeder Ausgabe gibt es eine Beilage mit jeweils einem bestimmten Wortschatz, eine Audio-CD und ein Übungsheft. Zusätzliches Material findet sich auf der Website www.kelvora-press.de.

Below the german version there should be a button with the text "Testexemplar bestellen"

Target Market(s)

People that want to improve their English skills for business

Industry/Entity Type

Business

Requirements
Must have
• The screenshots show the content of the screens and not how the items should be arranged.

```html
<!DOCTYPE html>
<html lang="de">
<head>
<meta charset="utf-8">
<title>TradeLingo – Heute</title>
<link rel="stylesheet" href="https://fonts.googleapis.com/css2?family=Arimo:wght@400;700&display=swap">
<style>
  :root {
    --page-bg: #f6f6f6;
    --status-top: #eef0f2;
    --status-bottom: #b9bec4;
    --status-text: #3a3d40;
    --app-blue: #396588;
    --app-blue-deep: #1f4a70;
    --app-blue-light: #6f9fc6;
    --brand-red: #872735;
    --header-red-top: #e0564d;
    --header-red: #b9302c;
    --header-red-bottom: #8f2424;
    --card-bg: #ffffff;
    --ink: #000000;
    --muted: #999999;
    --ad-black: #000000;
    --tab-bg: #1b1b1b;
    --tab-bg-top: #2d2d2d;
    --tab-active: #ffffff;
    --tab-idle: #999999;
    --white: #ffffff;
  }
  * { margin: 0; padding: 0; box-sizing: border-box; }
  html, body { width: 1200px; height: 2243px; overflow: hidden; background: var(--page-bg); }
  body { font-family: "Arimo", "Helvetica Neue", Arial, sans-serif; position: relative; }

  .app-screen {
    position: absolute; left: 0; top: 217px; width: 1200px; height: 1809px; overflow: hidden;
    background:
      linear-gradient(160deg, rgba(255,255,255,0.10) 0%, rgba(255,255,255,0) 35%),
      linear-gradient(200deg, rgba(255,255,255,0) 55%, rgba(120,180,230,0.25) 75%, rgba(255,255,255,0) 90%),
      linear-gradient(180deg, var(--app-blue) 0%, var(--app-blue-deep) 100%);
  }

  .status-bar {
    position: absolute; left: 0; top: 0; width: 1200px; height: 67px;
    background: linear-gradient(180deg, var(--status-top), var(--status-bottom));
    color: var(--status-text); font-weight: 700; font-size: 40px;
  }
  .status-bar .carrier { position: absolute; left: 16px; top: 12px; }
  .status-bar .wifi { position: absolute; left: 198px; top: 12px; }
  .status-bar .clock { position: absolute; left: 0; right: 0; top: 10px; text-align: center; font-size: 44px; color: #1a1a1a; }
  .status-bar .battery { position: absolute; right: 14px; top: 18px; }

  .app-header {
    position: absolute; left: 0; top: 174px; width: 1200px; height: 163px;
    background: linear-gradient(180deg, var(--header-red-top) 0%, var(--header-red) 45%, var(--header-red-bottom) 100%);
    box-shadow: 0 6px 14px rgba(0,0,0,0.35);
  }
  .app-title {
    color: var(--white); font-weight: 700; font-size: 72px; letter-spacing: -2px;
    text-align: center; line-height: 163px;
    text-shadow: 0 -2px 2px rgba(0,0,0,0.35);
  }

  .word-card {
    position: absolute; left: 29px; top: 377px; width: 1144px; height: 818px;
    background: var(--card-bg); border-radius: 36px;
  }
  .word-term { position: absolute; left: 49px; top: 40px; font-weight: 700; font-size: 80px; color: var(--ink); letter-spacing: -1px; }
  .word-type { font-size: 38px; letter-spacing: 0; }
  .word-translation { position: absolute; left: 49px; top: 192px; font-weight: 700; font-size: 41px; color: var(--ink); }
  .word-definition { position: absolute; left: 49px; top: 270px; font-weight: 700; font-size: 43px; color: var(--muted); }
  .word-example { position: absolute; left: 49px; top: 392px; font-weight: 700; font-size: 38px; line-height: 54px; color: var(--muted); }

  .play-button {
    position: absolute; left: 767px; top: 1231px; width: 406px; height: 118px;
    border-radius: 28px; color: var(--white); font-weight: 700; font-size: 43px;
    text-align: center; line-height: 118px;
    background: linear-gradient(180deg, var(--header-red-top) 0%, var(--header-red) 50%, var(--brand-red) 100%);
    box-shadow: 0 5px 12px rgba(0,0,0,0.4);
  }

  .ad-banner {
    position: absolute; left: 27px; top: 1396px; width: 1139px; height: 141px;
    background: linear-gradient(180deg, #2b2b2b 0%, var(--ad-black) 50%);
    border-radius: 14px; color: var(--white); font-weight: 700; font-size: 54px;
    text-align: center; line-height: 141px;
  }

  .tab-bar {
    position: absolute; left: 0; top: 1586px; width: 1200px; height: 223px;
    background: linear-gradient(180deg, var(--tab-bg-top) 0%, var(--tab-bg-top) 50%, var(--tab-bg) 50%, var(--tab-bg) 100%);
    display: flex;
  }
  .tab { flex: 1; position: relative; border-left: 2px solid rgba(255,255,255,0.05); }
  .tab:first-child { border-left: none; }
  .tab svg { position: absolute; left: 50%; top: 34px; transform: translateX(-50%); }
  .tab-label { position: absolute; left: 0; right: 0; top: 160px; text-align: center; font-weight: 700; font-size: 40px; color: var(--tab-idle); }
  .tab.is-active .tab-label { color: var(--tab-active); }
</style>
</head>
<body>
  <main class="app-screen">
    <div class="status-bar">
      <span class="carrier">Carrier</span>
      <svg class="wifi" width="62" height="44" viewBox="0 0 62 44">
        <g fill="none" stroke="#2f86c8" stroke-width="7" stroke-linecap="round">
          <path d="M5 15 Q31 -6 57 15"/>
          <path d="M15 25 Q31 11 47 25"/>
        </g>
        <circle cx="31" cy="36" r="6" fill="#2f86c8"/>
      </svg>
      <span class="clock">10:44 AM</span>
      <svg class="battery" width="90" height="34" viewBox="0 0 90 34">
        <rect x="2" y="2" width="78" height="30" rx="5" fill="none" stroke="#4a4a4a" stroke-width="3"/>
        <rect x="7" y="7" width="68" height="20" rx="2" fill="#3fc03a"/>
        <rect x="82" y="11" width="6" height="12" rx="2" fill="#4a4a4a"/>
      </svg>
    </div>

    <header class="app-header">
      <h1 class="app-title">TradeLingo</h1>
    </header>

    <article class="word-card">
      <h2 class="word-term">Hit the road <span class="word-type">(idiom)</span></h2>
      <p class="word-translation">Sich auf Weg machen</p>
      <p class="word-definition">To leave somewhere or set out on a journey</p>
      <p class="word-example">“Hey, Simon, come on, we’re going to be late.<br>Let’s hit the road!”</p>
    </article>

    <div class="play-button">Abspielen</div>

    <div class="ad-banner">Test Advertisement</div>

    <nav class="tab-bar">
      <div class="tab is-active">
        <svg width="112" height="112" viewBox="0 0 112 112">
          <rect x="18" y="22" width="80" height="80" rx="10" fill="#7e1b1b"/>
          <rect x="8" y="10" width="82" height="78" rx="10" fill="#d23a36"/>
          <rect x="18" y="30" width="62" height="48" rx="4" fill="#ffffff"/>
          <path d="M72 16 l8 8 M80 16 l-8 8" stroke="#fff" stroke-width="3"/>
        </svg>
        <span class="tab-label">Heute</span>
      </div>
      <div class="tab">
        <svg width="112" height="112" viewBox="0 0 112 112">
          <path d="M14 10 h84 v70 l-20 20 h-64 z" fill="#c9c9c9"/>
          <path d="M78 100 v-20 h20 z" fill="#8a8a8a"/>
          <path d="M48 26 h16 v26 h14 l-22 24 l-22 -24 h14 z" fill="#ffffff"/>
        </svg>
        <span class="tab-label">Archiv</span>
      </div>
      <div class="tab">
        <svg width="112" height="112" viewBox="0 0 112 112">
          <rect x="12" y="8" width="88" height="96" rx="10" fill="#3a3a3a" stroke="#bdbdbd" stroke-width="5"/>
          <g fill="#d8d8d8">
            <rect x="28" y="28" width="8" height="6"/><rect x="42" y="28" width="42" height="6"/>
            <rect x="28" y="44" width="8" height="6"/><rect x="42" y="44" width="42" height="6"/>
            <rect x="28" y="60" width="8" height="6"/><rect x="42" y="60" width="42" height="6"/>
            <rect x="28" y="76" width="8" height="6"/><rect x="42" y="76" width="42" height="6"/>
          </g>
        </svg>
        <span class="tab-label">A-Z</span>
      </div>
      <div class="tab">
        <svg width="112" height="112" viewBox="0 0 112 112">
          <path d="M14 8 h84 v74 l-20 22 h-64 z" fill="#f0f0f0"/>
          <path d="M78 104 v-22 h20 z" fill="#a8a8a8"/>
          <g fill="#8a8a8a">
            <rect x="26" y="24" width="60" height="5"/><rect x="26" y="38" width="60" height="5"/>
            <rect x="26" y="52" width="60" height="5"/><rect x="26" y="66" width="46" height="5"/>
          </g>
        </svg>
        <span class="tab-label">Info</span>
      </div>
    </nav>
  </main>
</body>
</html>
```